Personal Finance Blog Wordpress Design

We are looking for a new Wordpress theme design for CoinHarbor.com.

All of the elements that are currently on the homepage should remain, minus the archives list. The placement of various elements can be changed, we just need a more modern and clean feel. We would like to add a 160 x 600 ad unit on the homepage. We would like the 728x90 ad to be below the navigation similar to that of: http://www.plumtreeledger.example/blog/

We like the fonts used on: http://www.quillpocket.example/blog/

The text that currently resides at the bottom of CoinHarbor.com needs to remain on the homepage, but wherever it is placed needs to not be intrusive.

The color scheme needs to appropriately compliment the logo.

No sliders. I don't like sliders.

I am happy to answer questions.

Industry/Entity Type

Finance

Requirements
Must have
• Included in project description
Nice to have
Should not have
• Included in project description. Don't use sliders

```html
<!DOCTYPE html>
<html lang="en">
<head>
<meta charset="utf-8">
<title>CoinHarbor – Personal Finance Blog</title>
<link href="https://fonts.googleapis.com/css2?family=Raleway:wght@400;500;600;700&family=Open+Sans:wght@400;600&display=swap" rel="stylesheet">
<style>
:root{
  --green:#8cc63f;
  --green-dark:#3f8b17;
  --green-deep:#2e6b0f;
  --bg:#f0f0ee;
  --card:#ffffff;
  --line:#e3e3e3;
  --text:#333333;
  --muted:#777777;
  --meta:#7cb82f;
}
*{box-sizing:border-box;margin:0;padding:0}
html,body{width:1200px;height:3175px;overflow:hidden}
body{background:var(--bg);font-family:"Open Sans",Arial,sans-serif;color:var(--text);position:relative}
a{color:inherit;text-decoration:none}
.topline{position:absolute;left:0;top:0;width:100%;height:4px;background:var(--green-deep)}
.site-header{position:absolute;left:0;top:4px;width:100%;height:83px;background:#fff;display:flex;align-items:center;justify-content:center}
.brand{display:flex;align-items:center;gap:10px;font-family:"Raleway",sans-serif;font-weight:700;font-size:22px;color:var(--green-dark)}
.brand-mark{width:22px;height:22px;background:var(--green-dark)}
.main-nav{position:absolute;left:0;top:87px;width:100%;height:48px;background:var(--green)}
.main-nav ul{list-style:none;display:flex;width:1000px;margin:0 auto;height:100%}
.main-nav li{flex:auto;display:flex;align-items:center;justify-content:center;color:#fff;font-family:"Raleway",sans-serif;font-size:14px;border-left:1px solid rgba(255,255,255,.35)}
.main-nav li:last-child{border-right:1px solid rgba(255,255,255,.35)}
.leader-ad{position:absolute;left:288px;top:167px;width:624px;height:78px;background:linear-gradient(90deg,#1d5fa8,#3a8fd6 60%,#1f62a6);display:flex;align-items:center;border:1px solid #1a4f8a}
.leader-ad .photo{width:70px;height:100%;background:linear-gradient(#e9c9a8,#c99a74)}
.leader-ad .head{flex:1;color:#fff;font-family:"Raleway",sans-serif;font-weight:700;font-size:17px;padding-left:12px}
.leader-ad .free{background:#f3c21b;color:#222;font-weight:700;font-family:"Raleway",sans-serif;font-size:22px;padding:6px 16px;border-radius:4px;margin-right:16px}
.leader-ad .tag{background:#2f8a2c;color:#fff;font-family:"Raleway",sans-serif;font-weight:700;font-style:italic;font-size:19px;line-height:22px;height:100%;width:170px;display:flex;align-items:center;justify-content:center;text-align:center}
.box{background:var(--card);border:1px solid var(--line)}
.featured{position:absolute;left:100px;top:277px;width:704px;height:544px}
.featured .lead-img{position:absolute;left:18px;top:26px;width:333px;height:290px;background:linear-gradient(135deg,#e6e1a4,#c5cf87 50%,#9fb36a)}
.featured .lead-title{position:absolute;left:18px;top:334px;width:340px;font-family:"Raleway",sans-serif;font-size:24px;line-height:32px;color:var(--green-dark);font-weight:500}
.featured .lead-title b{font-weight:700}
.meta{font-size:11px;color:var(--meta)}
.featured .lead-meta{position:absolute;left:18px;top:418px}
.featured .lead-text{position:absolute;left:18px;top:450px;width:330px;font-size:11.5px;line-height:17px;color:var(--muted)}
.side-list{position:absolute;left:374px;top:28px;width:310px}
.side-item{display:flex;gap:22px;height:129px;border-bottom:1px solid var(--line);padding-top:0}
.side-item:last-child{border-bottom:0}
.side-item .thumb{width:89px;height:89px;flex:none}
.side-item h3{font-family:"Raleway",sans-serif;font-weight:500;font-size:13px;color:#222;margin:2px 0 4px}
.side-item p{font-size:11px;line-height:17px;color:var(--muted);margin-top:4px}
.grid{position:absolute;left:100px;top:857px;width:704px;display:grid;grid-template-columns:333px 333px;column-gap:38px}
.card{position:relative;height:417px;margin-bottom:46px}
.card:nth-child(3),.card:nth-child(4){margin-bottom:36px}
.card:nth-child(5),.card:nth-child(6){margin-bottom:44px}
.card .img{height:216px}
.card .label{position:absolute;left:18px;top:-6px;background:var(--green);color:#fff;font-family:"Raleway",sans-serif;font-size:14px;padding:4px 14px}
.card h2{font-family:"Raleway",sans-serif;font-weight:600;font-size:18px;line-height:24px;color:var(--green-deep);margin:24px 18px 8px}
.card .meta{margin:0 18px}
.card p{font-size:11.5px;line-height:18px;color:var(--muted);margin:8px 18px 14px}
.card .more{font-family:"Raleway",sans-serif;font-weight:600;font-size:12px;color:var(--green-dark);margin:0 18px;display:flex;align-items:center;gap:5px}
.about{position:absolute;left:100px;top:2675px;width:704px;height:258px;background:var(--green);color:#fff;padding:22px 18px}
.about h2{font-family:"Raleway",sans-serif;font-weight:500;font-size:24px;margin-bottom:16px}
.about h2 b{font-weight:700}
.about p{font-size:11.5px;line-height:20px;margin-bottom:12px}
.pager{position:absolute;left:100px;top:2971px;display:flex;gap:9px;align-items:center}
.pager span{width:32px;height:32px;display:flex;align-items:center;justify-content:center;background:#fff;border:1px solid var(--line);font-size:13px}
.pager .current{background:var(--green-deep);color:#fff;border-color:var(--green-deep)}
.pager .dots{border:0;background:none;width:auto;letter-spacing:2px}
.sidebar .widget{position:absolute;left:838px;width:262px}
.widget h4{font-family:"Raleway",sans-serif;font-weight:500;font-size:19px;color:var(--green-deep);margin-bottom:10px}
.connect{top:277px;height:106px;padding:16px 16px}
.socials{display:flex;gap:10px}
.socials span{width:38px;height:38px;background:#eeeeee;border:1px solid #e0e0e0}
.socials span:first-child{background:var(--green);border-color:var(--green)}
.newsletter{top:400px;height:173px;padding:16px}
.newsletter p{font-size:11.5px;line-height:17px;color:var(--muted);margin-bottom:10px}
.field{height:46px;border:1px solid #dcdcdc;display:flex;align-items:center;justify-content:space-between;padding:0 16px;font-size:12px;color:#888;background:#fff}
.search{top:592px;height:121px;padding:16px;background:var(--green);border-color:var(--green)}
.search h4{color:#fff}
.recent{top:732px;height:563px;padding:22px 16px}
.recent-item{display:flex;gap:14px;height:98px}
.recent-item .thumb{width:78px;height:74px;flex:none}
.recent-item h5{font-family:"Open Sans",sans-serif;font-weight:400;font-size:12px;line-height:17px;color:#333;margin-top:4px}
.recent-item .meta{display:block;margin-top:2px}
.sky-ad{position:absolute;left:903px;top:1318px;width:138px;height:515px;background:#fff;border:1px solid #ccc;padding:8px}
.sky-ad .brandbar{font-family:"Raleway",sans-serif;font-weight:700;font-size:12px;color:#f07c1e}
.sky-ad .phones{height:200px;margin:10px 0;background:linear-gradient(#dfe8e8,#2b2b2b)}
.sky-ad h6{font-family:"Raleway",sans-serif;font-weight:700;font-size:17px;line-height:19px;color:#2f8a2c}
.sky-ad p{font-size:11px;color:#333;margin:8px 0}
.sky-ad .btn{background:#d4202b;color:#fff;font-size:10px;font-weight:600;padding:5px 6px;display:inline-block}
.sky-ad small{display:block;font-size:7px;color:#777;margin-top:28px;line-height:9px}
.site-footer{position:absolute;left:0;top:3058px;width:100%;height:117px;background:#fff;border-top:1px solid var(--line);text-align:center}
.site-footer nav{margin-top:32px;font-size:12px;color:#555}
.site-footer nav span{padding:0 8px;border-right:1px solid #aaa}
.site-footer nav span:last-child{border:0}
.site-footer .copy{margin-top:16px;font-size:11px;color:#666}
.bottomline{position:absolute;left:0;bottom:0;width:100%;height:6px;background:var(--green)}
.t1{background:linear-gradient(135deg,#6b7a86,#c9d3d8)}
.t2{background:linear-gradient(135deg,#b9c6cf,#7d8c97)}
.t3{background:linear-gradient(135deg,#cfd6da,#8b98a1)}
.t4{background:linear-gradient(135deg,#4d6f8e,#2b3e52)}
</style>
</head>
<body>
<div class="topline"></div>
<header class="site-header">
  <div class="brand"><span class="brand-mark"></span>CoinHarbor</div>
</header>
<nav class="main-nav">
  <ul>
    <li>Auto</li><li>Bank Accounts</li><li>Credit Cards</li><li>Insurance</li><li>Investments</li><li>Mortgages</li><li>Personal Finance</li><li>Small Business</li><li>Taxes</li>
  </ul>
</nav>

<div class="leader-ad">
  <div class="photo" role="img" aria-label="Smiling woman portrait"></div>
  <div class="head">The Next Generation in Self-Development!<br><span style="font-size:13px">Life Toolkit</span></div>
  <div class="free">FREE!</div>
  <div class="tag">Changing<br>Lives Together</div>
</div>

<section class="featured box">
  <div class="lead-img" role="img" aria-label="Budget charts with pen and glasses on paperwork"></div>
  <h1 class="lead-title">Best Budgeting <b>Software</b> for 2015</h1>
  <div class="meta lead-meta">Apr 28th, 2015 · 0 Comment</div>
  <p class="lead-text">As businesses everywhere look to find new and more efficient ways to develop their budgets in 2015, much of their attention is focused on finding...</p>
  <div class="side-list">
    <article class="side-item"><div class="thumb t4" role="img" aria-label="Hand with pen over charts"></div><div><h3>Stellar Radio Stock: How it Fares</h3><div class="meta">Apr 28th, 2015 · 0 Comment</div><p>As the days of satellite radio seem numbered, there seems to...</p></div></article>
    <article class="side-item"><div class="thumb t3" role="img" aria-label="Financial charts on desk"></div><div><h3>Stellar Radio Stock: How it Fares</h3><div class="meta">Apr 28th, 2015 · 0 Comment</div><p>As the days of satellite radio seem numbered, there seems to...</p></div></article>
    <article class="side-item"><div class="thumb t2" role="img" aria-label="Business handshake"></div><div><h3>Stellar Radio Stock: How it Fares</h3><div class="meta">Apr 28th, 2015 · 0 Comment</div><p>As the days of satellite radio seem numbered, there seems to...</p></div></article>
    <article class="side-item"><div class="thumb t4" role="img" aria-label="Hand pointing at a screen"></div><div><h3>Stellar Radio Stock: How it Fares</h3><div class="meta">Apr 28th, 2015 · 0 Comment</div><p>As the days of satellite radio seem numbered, there seems to...</p></div></article>
  </div>
</section>

<main class="grid">
  <article class="card box"><div class="img" role="img" aria-label="Woman beside a broken-down car on a desert road" style="background:linear-gradient(#c8d6e2,#9a8f7a 60%,#6d6252)"></div><span class="label">Auto</span><h2>7 Cars With Good Gas Mileage</h2><div class="meta">Apr 28th, 2015 · 0 Comment</div><p>Fuel efficient vehicles can save you money, reduce the need to stop for gas as often, and benefit the environment. In many cases,</p><a class="more">Raed More <svg width="6" height="8"><path d="M0 0L6 4L0 8Z" fill="currentColor"/></svg></a></article>
  <article class="card box"><div class="img" role="img" aria-label="Adviser explaining documents to an older couple" style="background:linear-gradient(135deg,#d9d6cf,#8f9aa6)"></div><span class="label">Bank Accounts</span><h2>Want to Increase Your Savings? Check Out These Great....</h2><div class="meta">Apr 28th, 2015 · 0 Comment</div><p>Fuel efficient vehicles can save you money, reduce the need to stop for gas as often, ....</p><a class="more">Raed More <svg width="6" height="8"><path d="M0 0L6 4L0 8Z" fill="currentColor"/></svg></a></article>
  <article class="card box"><div class="img" role="img" aria-label="Woman with glasses using a laptop by a bookshelf" style="background:linear-gradient(135deg,#c9a27a,#e8e2d8 60%,#b5b8a0)"></div><span class="label">Credit Cards</span><h2>7 Cars With Good Gas Mileage</h2><div class="meta">Apr 28th, 2015 · 0 Comment</div><p>Fuel efficient vehicles can save you money, reduce the need to stop for gas as often, and benefit the environment. In many cases,</p><a class="more">Raed More <svg width="6" height="8"><path d="M0 0L6 4L0 8Z" fill="currentColor"/></svg></a></article>
  <article class="card box"><div class="img" role="img" aria-label="Piggy bank on grass under a blue sky" style="background:linear-gradient(#3f86d6,#bcd9f0 55%,#6fae2e 75%)"></div><span class="label">Insurance</span><h2>Want to Increase Your Savings? Check Out These Great....</h2><div class="meta">Apr 28th, 2015 · 0 Comment</div><p>Fuel efficient vehicles can save you money, reduce the need to stop for gas as often, ....</p><a class="more">Raed More <svg width="6" height="8"><path d="M0 0L6 4L0 8Z" fill="currentColor"/></svg></a></article>
  <article class="card box"><div class="img" role="img" aria-label="Couple with a pink piggy bank and coins" style="background:linear-gradient(135deg,#e6e3de,#b3a596)"></div><span class="label">Investments</span><h2>7 Cars With Good Gas Mileage</h2><div class="meta">Apr 28th, 2015 · 0 Comment</div><p>Fuel efficient vehicles can save you money, reduce the need to stop for gas as often, and benefit the environment. In many cases,</p><a class="more">Raed More <svg width="6" height="8"><path d="M0 0L6 4L0 8Z" fill="currentColor"/></svg></a></article>
  <article class="card box"><div class="img" role="img" aria-label="Model house on a desk with business people" style="background:linear-gradient(135deg,#2f4f6a,#8fa4b5 60%,#c9d2d8)"></div><span class="label">Mortgages</span><h2>Want to Increase Your Savings? Check Out These Great....</h2><div class="meta">Apr 28th, 2015 · 0 Comment</div><p>Fuel efficient vehicles can save you money, reduce the need to stop for gas as often, ....</p><a class="more">Raed More <svg width="6" height="8"><path d="M0 0L6 4L0 8Z" fill="currentColor"/></svg></a></article>
  <article class="card box"><div class="img" role="img" aria-label="Blue stock market chart with a pen" style="background:linear-gradient(135deg,#1d5fa0,#9ccbee 60%,#e8f3fb)"></div><span class="label">Personal Finance</span><h2>7 Cars With Good Gas Mileage</h2><div class="meta">Apr 28th, 2015 · 0 Comment</div><p>Fuel efficient vehicles can save you money, reduce the need to stop for gas as often, and benefit the environment. In many cases,</p><a class="more">Raed More <svg width="6" height="8"><path d="M0 0L6 4L0 8Z" fill="currentColor"/></svg></a></article>
  <article class="card box"><div class="img" role="img" aria-label="Businesswoman holding a tablet outside an office" style="background:linear-gradient(135deg,#cfdbe6,#f2f4f6 50%,#8ea6bf)"></div><span class="label">Small Business</span><h2>Want to Increase Your Savings? Check Out These Great....</h2><div class="meta">Apr 28th, 2015 · 0 Comment</div><p>Fuel efficient vehicles can save you money, reduce the need to stop for gas as often, ....</p><a class="more">Raed More <svg width="6" height="8"><path d="M0 0L6 4L0 8Z" fill="currentColor"/></svg></a></article>
</main>

<section class="about">
  <h2>Coin Harbor: Personal <b>Finance</b> Blog</h2>
  <p>Our mission is to enrich the lives of our readers (literally!) by providing the very best personal finance content on the internet. Our readers may be at different stages in life, with different personal finance situations and needs. One person may be looking to get their first credit card, another might be looking into how to get a mortgage.</p>
  <p>A home, some may be looking for ways to afford or finance a college education for themselves or their children, many want to know how to improve their credit score, and still others might be planning for retirement. And just about everyone can benefit from information about saving money and creating a family budget can draw off the experiences of each other and contribute to everyone's success.</p>
</section>

<div class="pager"><span class="current">1</span><span>2</span><span>3</span><span>4</span><span class="dots">.......</span><span>13</span></div>

<aside class="sidebar">
  <div class="widget box connect">
    <h4>Connect with us online</h4>
    <div class="socials"><span></span><span></span><span></span><span></span><span></span></div>
  </div>
  <div class="widget box newsletter">
    <h4>E-mail Newsletter</h4>
    <p>Sign up now to receive breaking news and to hear what's new with our...</p>
    <div class="field">Email address <svg width="16" height="11" viewBox="0 0 16 11"><rect width="16" height="11" rx="1" fill="#8cc63f"/><path d="M1 1L8 6L15 1" stroke="#fff" fill="none" stroke-width="1.3"/></svg></div>
  </div>
  <div class="widget box search">
    <h4>Search CoinHarbor</h4>
    <div class="field">Enter Key word <svg width="14" height="14" viewBox="0 0 14 14"><circle cx="6" cy="6" r="4.5" stroke="#8cc63f" stroke-width="2" fill="none"/><path d="M9.5 9.5L13 13" stroke="#8cc63f" stroke-width="2"/></svg></div>
  </div>
  <div class="widget box recent">
    <h4 style="margin-bottom:20px">Recent Posts</h4>
    <div class="recent-item"><div class="thumb t3" role="img" aria-label="Budget papers"></div><div><h5>Best Budgeting Software for 2015</h5><span class="meta">April 29,2015</span></div></div>
    <div class="recent-item"><div class="thumb t4" role="img" aria-label="Stock chart"></div><div><h5>Stellar Radio Stock: How it Fares in 2015</h5><span class="meta">April 29,2015</span></div></div>
    <div class="recent-item"><div class="thumb t2" role="img" aria-label="House for sale"></div><div><h5>Financial Benefits of Buying Foreclosed</h5><span class="meta">April 29,2015</span></div></div>
    <div class="recent-item"><div class="thumb" style="background:linear-gradient(135deg,#3b2a1a,#d9a441)" role="img" aria-label="Coins and jar"></div><div><h5>Want to Increase Your Savings?</h5><span class="meta">April 29,2015</span></div></div>
    <div class="recent-item"><div class="thumb" style="background:linear-gradient(135deg,#b58b6c,#e9dccf)" role="img" aria-label="Woman shopping"></div><div><h5>5 Appliances on Sale to Save Money</h5><span class="meta">April 29,2015</span></div></div>
  </div>
  <div class="sky-ad">
    <div class="brandbar">peak</div>
    <div class="phones" role="img" aria-label="Two smartphones"></div>
    <h6>Holidays Revolve Around Nova.</h6>
    <p>$20 Off Nova Orbit Phone</p>
    <span class="btn">Spread Some Joy &gt;</span>
    <small>Promo code: SAVE20 offer ends soon, terms apply.</small>
  </div>
</aside>

<footer class="site-footer">
  <nav><span>Home</span><span>Personal Finance</span><span>Mortgages</span><span>Bank Accounts</span><span>Credit Cards</span><span>Insurance</span><span>Auto Investments</span><span>Taxes</span><span>Small Business</span></nav>
  <div class="copy">© 2015 Coin Harbor. All rights reserved. | Contact Us | Privacy Policy | Terms and Conditions</div>
  <div class="bottomline"></div>
</footer>
</body>
</html>
```